Top of the line business card design needed for real estate brokerage

We currently have a business card with our logo but would like to have a revised version. We would love for you to implement your own design that will catch anyone's attention. The theme colors should be black, royal blue, gray/silver, and white.The contact information should be the same as the info on our current business card (picture attached). In the design that we pick, we will need to be able to edit the text so that we can customize the text content for each of our agents. Same goes for the professional picture. There should be an area on the card that each agent can have their professional portrait attached. Please include a version without the picture option as well for agents that do not wish to have a professional picture attached.
Business

```html
<!DOCTYPE html>
<html lang="en">
<head>
<meta charset="utf-8">
<title>Clearstone Realty – Business Cards</title>
<link href="https://fonts.googleapis.com/css2?family=Open+Sans:ital,wght@0,400;0,600;0,700;1,400&display=swap" rel="stylesheet">
<style>
  :root {
    --backdrop: #ebebeb;
    --card: #ffffff;
    --royal-blue: #3a6cc4;
    --ink: #1e1e1e;
    --body-text: #2b2b2b;
    --silver: #b9bcc2;
    --silver-light: #eceef1;
    --silver-mid: #dcdfe4;
    --shadow: rgba(0, 0, 0, 0.16);
  }
  * { box-sizing: border-box; margin: 0; padding: 0; }
  html, body {
    width: 848px; height: 1200px; overflow: hidden;
    background: var(--backdrop);
    font-family: "Open Sans", Arial, sans-serif;
  }
  .sheet { position: relative; width: 848px; height: 1200px; }

  .card {
    position: absolute;
    width: 370px; height: 212px;
    background: var(--card);
    box-shadow: 0 14px 30px var(--shadow);
    overflow: hidden;
  }
  .card--front-plain { left: 36px; top: 170px; }
  .card--back-a      { left: 442px; top: 300px; }
  .card--front-photo { left: 36px; top: 720px; }
  .card--back-b      { left: 442px; top: 850px; }

  /* brand wordmark */
  .brand {
    display: flex; align-items: center; gap: 7px;
    font-weight: 600; color: var(--ink);
    white-space: nowrap;
  }
  .brand__square { width: 10px; height: 10px; background: var(--royal-blue); flex: none; }
  .card__brand { position: absolute; right: 22px; top: 24px; font-size: 15px; }

  /* agent block */
  .agent { position: absolute; left: 26px; bottom: 22px; }
  .agent--with-photo { left: 112px; }
  .agent__name { font-size: 19px; font-weight: 700; color: var(--royal-blue); line-height: 1.1; }
  .agent__title { font-size: 10px; font-style: italic; color: var(--royal-blue); margin: 1px 0 10px 14px; }
  .agent__address { font-size: 10px; color: var(--body-text); line-height: 1.35; margin-bottom: 9px; }
  .contact-list { list-style: none; }
  .contact-list li {
    display: flex; align-items: center; gap: 7px;
    font-size: 10px; color: var(--body-text); line-height: 1.55;
  }
  .contact-list svg { width: 9px; height: 9px; fill: var(--ink); flex: none; }

  .portrait {
    position: absolute; left: 26px; bottom: 70px;
    width: 70px; height: 70px; border-radius: 50%;
    background: radial-gradient(circle at 50% 40%, #d9d4cf 0%, #9b938d 60%, #4a4745 100%);
    border: 3px solid var(--silver-light);
  }

  /* back side */
  .skyline {
    position: absolute; inset: 0;
    background:
      radial-gradient(ellipse 70% 60% at 50% 70%, var(--silver-mid) 0%, rgba(220,223,228,0) 100%),
      linear-gradient(180deg, var(--card) 0%, var(--silver-light) 55%, var(--silver-mid) 100%);
  }
  .card__brand--large {
    position: absolute; left: 50%; top: 50%;
    transform: translate(-50%, -50%);
    font-size: 30px; gap: 12px;
  }
  .card__brand--large .brand__square { width: 18px; height: 18px; }
</style>
</head>
<body>
<main class="sheet">

  <!-- Front, no portrait -->
  <section class="card card--front-plain">
    <div class="brand card__brand"><span class="brand__square"></span>Clearstone Realty</div>
    <div class="agent">
      <h1 class="agent__name">Marcus Delaney</h1>
      <p class="agent__title">Broker</p>
      <p class="agent__address">2200 Harbor Point Ave, Suite 310<br>Coral Bay, FL 33190</p>
      <ul class="contact-list">
        <li><svg viewBox="0 0 10 10"><path d="M2 0.5 L3.6 2.6 L2.8 3.6 Q4 6 6.4 7.2 L7.4 6.4 L9.5 8 L8.4 9.5 Q2.5 9 0.5 1.6 Z"/></svg>555 - 014 - 2768</li>
        <li><svg viewBox="0 0 10 10"><path d="M0 2 H10 V8.5 H0 Z M0.8 2.6 L5 5.8 L9.2 2.6 Z" fill-rule="evenodd"/></svg>marcus@clearstonerealty.com</li>
        <li><svg viewBox="0 0 10 10"><circle cx="5" cy="5" r="4.5"/><path d="M0.5 5 H9.5 M5 0.5 V9.5" stroke="#fff" stroke-width="0.8"/></svg>clearstonerealty.com</li>
      </ul>
    </div>
  </section>

  <!-- Back -->
  <section class="card card--back-a">
    <div class="skyline" role="img" aria-label="Light gray line drawing of a city skyline"></div>
    <div class="brand card__brand--large"><span class="brand__square"></span>Clearstone Realty</div>
  </section>

  <!-- Front, with portrait -->
  <section class="card card--front-photo">
    <div class="brand card__brand"><span class="brand__square"></span>Clearstone Realty</div>
    <div class="portrait" role="img" aria-label="Agent's circular professional portrait"></div>
    <div class="agent agent--with-photo">
      <h2 class="agent__name">Marcus Delaney</h2>
      <p class="agent__title">Broker</p>
      <p class="agent__address">2200 Harbor Point Ave, Suite 310<br>Coral Bay, FL 33190</p>
      <ul class="contact-list">
        <li><svg viewBox="0 0 10 10"><path d="M2 0.5 L3.6 2.6 L2.8 3.6 Q4 6 6.4 7.2 L7.4 6.4 L9.5 8 L8.4 9.5 Q2.5 9 0.5 1.6 Z"/></svg>555 - 014 - 2768</li>
        <li><svg viewBox="0 0 10 10"><path d="M0 2 H10 V8.5 H0 Z M0.8 2.6 L5 5.8 L9.2 2.6 Z" fill-rule="evenodd"/></svg>marcus@clearstonerealty.com</li>
        <li><svg viewBox="0 0 10 10"><circle cx="5" cy="5" r="4.5"/><path d="M0.5 5 H9.5 M5 0.5 V9.5" stroke="#fff" stroke-width="0.8"/></svg>clearstonerealty.com</li>
      </ul>
    </div>
  </section>

  <!-- Back -->
  <section class="card card--back-b">
    <div class="skyline" role="img" aria-label="Light gray line drawing of a city skyline"></div>
    <div class="brand card__brand--large"><span class="brand__square"></span>Clearstone Realty</div>
  </section>

</main>
</body>
</html>
```